Need Business Card for our Real Estate Business with Sales Executive's Picture

PANTONE 484 C ( RED)

PANTONE 2766 C ( BLUE

Industry/Entity Type

Real Estate

Contact Information for Business Card

Name, Mobile, email, & picture of Person
Agency Phone, address, Web address

Requirements
Must have
• Our Logo Colours, Agent Picture,

```html
<!DOCTYPE html>
<html lang="en">
<head>
<meta charset="utf-8">
<title>Meridian Business Card</title>
<link rel="stylesheet" href="https://fonts.googleapis.com/css2?family=Ubuntu:wght@400;500;700&display=swap">
<style>
  :root {
    --navy: #0e1a3d;
    --brand-blue: #261c6b;
    --brand-red: #a33224;
    --paper: #ffffff;
    --ink: #1f1a5c;
    --stage: #f4f4f6;
    --photo: #9a9ca3;
  }
  * { box-sizing: border-box; margin: 0; padding: 0; }
  html, body {
    width: 1200px; height: 872px; overflow: hidden;
    background: var(--stage);
    font-family: "Ubuntu", sans-serif;
  }
  .sheet {
    width: 1200px; height: 872px;
    display: flex; align-items: center; justify-content: center; gap: 40px;
  }
  .card {
    position: relative;
    width: 540px; height: 309px;
    overflow: hidden;
    box-shadow: 0 10px 30px rgba(0,0,0,.15);
  }
  /* front */
  .card--front { background: var(--navy); display: flex; align-items: center; justify-content: center; }
  .brand { display: flex; align-items: center; gap: 10px; }
  .brand__mark { width: 9px; height: 9px; background: var(--brand-red); }
  .brand__name { font-weight: 400; letter-spacing: .28em; }
  .card--front .brand__name { color: var(--paper); font-size: 30px; }

  /* back */
  .card--back { background: var(--paper); }
  .card--back .brand { position: absolute; left: 30px; top: 28px; }
  .card--back .brand__name { color: var(--ink); font-size: 15px; }
  .card--back .brand__mark { width: 6px; height: 6px; }

  .contact { position: absolute; left: 30px; top: 86px; color: var(--ink); }
  .contact__name { font-size: 17px; font-weight: 700; padding-bottom: 6px; border-bottom: 2px solid var(--brand-red); width: 190px; margin-bottom: 12px; }
  .contact__list { list-style: none; display: flex; flex-direction: column; gap: 9px; font-size: 14px; font-weight: 500; }
  .contact__item { display: flex; align-items: center; gap: 8px; }
  .contact__icon { width: 18px; height: 18px; border-radius: 50%; background: var(--ink); display: flex; align-items: center; justify-content: center; }
  .contact__icon svg { width: 10px; height: 10px; }

  .accent-band {
    position: absolute; inset: 0;
    background: var(--brand-blue);
    clip-path: polygon(82% 0, 100% 0, 100% 100%, 60% 100%, 56% 78%, 82% 30%);
  }
  .portrait-frame {
    position: absolute; left: 322px; top: 100px;
    width: 150px; height: 140px;
    background: var(--paper); padding: 7px;
    box-shadow: 0 3px 10px rgba(0,0,0,.25);
  }
  .portrait { width: 100%; height: 100%; background: linear-gradient(160deg, #b3b5bb, var(--photo)); }
</style>
</head>
<body>
<main class="sheet">
  <section class="card card--front" aria-label="Business card front">
    <div class="brand">
      <span class="brand__mark"></span>
      <span class="brand__name">MERIDIAN</span>
    </div>
  </section>

  <section class="card card--back" aria-label="Business card back">
    <div class="accent-band"></div>
    <div class="brand">
      <span class="brand__mark"></span>
      <span class="brand__name">MERIDIAN</span>
    </div>
    <div class="contact">
      <p class="contact__name">Name Surname</p>
      <ul class="contact__list">
        <li class="contact__item">
          <span class="contact__icon"><svg viewBox="0 0 10 10"><path d="M2 1 L4 1 L4.6 3 L3.5 3.8 Q4.5 5.8 6.2 6.5 L7 5.4 L9 6 L9 8 Q5 9 1.5 4.5 Q1 2.5 2 1Z" fill="#fff"/></svg></span>
          +0123456789
        </li>
        <li class="contact__item">
          <span class="contact__icon"><svg viewBox="0 0 10 10"><rect x="1" y="2.5" width="8" height="5.5" fill="none" stroke="#fff" stroke-width="1"/><path d="M1 2.5 L5 5.5 L9 2.5" fill="none" stroke="#fff" stroke-width="1"/></svg></span>
          email@email.com
        </li>
        <li class="contact__item">
          <span class="contact__icon"><svg viewBox="0 0 10 10"><path d="M5 9.5 L2.2 5.2 A3.2 3.2 0 1 1 7.8 5.2 Z" fill="#fff"/><circle cx="5" cy="3.8" r="1.1" fill="#1f1a5c"/></svg></span>
          Adress Street No1, City
        </li>
      </ul>
    </div>
    <div class="portrait-frame">
      <div class="portrait" role="img" aria-label="Portrait photo of the sales executive"></div>
    </div>
  </section>
</main>
</body>
</html>
```